High-end construction company needs a business card design

We need a modern looking business card that draws people in, is memorable and looks so good people will want to sick it on their fridges.
On the first side what is needed are:
Logo
My name - Tomas Verbelk
Title - Managing Director
Website - www.kravel.co.uk
Email - tomas@kravel.co.uk
Telephone - 020 5194 6381
Mobile - 07845319027
On the back side was is needed is a list of all the services we provide:
-Kitchen Renovations
-Bathroom Renovations
-House Renovations
-Garage Conversions
-Extensions
-Loft Conversions
-Conservatories
-Carpentry
-Tiling
-Electrical
-Plumbing & Heating
-Bricklaying
-Landscaping
-Decorating
-Plastering
We would like the colours to be the same shades as on the logo with grey or black for the words.
Target Market(s)
Anyone who needs building work done
Contact Information for Business Card
This business card is for a construction company which strives to deliver excellent service and quality.
The look and feel of the card should represent this.
Requirements
Must have
- On the first side what is needed are:
Logo
My name - Tomas Verbelk
Title - Managing Director
Website - www.kravel.co.uk
Email - tomas@kravel.co.uk
Telephone - 020 5194 6381
Mobile - 07845319027
Nice to have
- Cool looking features

```html
<!DOCTYPE html>
<html lang="en">
<head>
<meta charset="utf-8">
<title>Kravel Construction – Services</title>
<link href="https://fonts.googleapis.com/css2?family=Montserrat:wght@500;600;700;800;900&display=swap" rel="stylesheet">
<style>
  :root {
    --green: #6bb043;
    --green-tone-a: #7dbd52;
    --green-tone-b: #9fd077;
    --white: #ffffff;
    --paper: #ffffff;
    --ink: #5f8d45;
    --grey: #4a4a4a;
  }
  html, body {
    margin: 0;
    padding: 0;
    overflow: hidden;
    background: var(--paper);
  }
  .card {
    position: relative;
    width: 1200px;
    height: 750px;
    overflow: hidden;
    background: var(--paper);
    font-family: "Montserrat", Arial, sans-serif;
  }
  .card__shapes {
    position: absolute;
    inset: 0;
  }
  .contact {
    position: absolute;
    left: 40px;
    top: 36px;
    color: var(--grey);
    font-size: 15px;
    line-height: 1.45;
    font-weight: 500;
  }
  .contact__name {
    margin: 0;
    color: var(--ink);
    font-size: 22px;
    font-weight: 800;
  }
  .contact__title {
    margin: 0 0 6px;
    font-size: 13px;
    font-weight: 700;
    letter-spacing: 1px;
    text-transform: uppercase;
  }
  .contact__line {
    margin: 0;
  }
  .brand {
    position: absolute;
    left: 96px;
    top: 236px;
    display: flex;
    align-items: center;
    gap: 8px;
    color: var(--ink);
    font-weight: 800;
    font-size: 26px;
    letter-spacing: 1px;
  }
  .brand__mark {
    width: 18px;
    height: 18px;
    background: var(--ink);
  }
  .heading {
    position: absolute;
    left: 40px;
    top: 552px;
    margin: 0;
    transform-origin: 0 0;
    transform: rotate(-45deg);
    color: var(--white);
    font-weight: 900;
    font-size: 88px;
    line-height: 1;
    letter-spacing: 2px;
    white-space: nowrap;
  }
  .website {
    position: absolute;
    left: 132px;
    top: 600px;
    transform-origin: 0 0;
    transform: rotate(-45deg);
    color: var(--white);
    font-weight: 600;
    font-size: 34px;
    line-height: 1;
    white-space: nowrap;
  }
  .services {
    list-style: none;
    margin: 0;
    padding: 0;
  }
  .services__item {
    position: absolute;
    transform-origin: 0 0;
    transform: rotate(45deg);
    color: var(--white);
    font-weight: 700;
    font-size: 20px;
    line-height: 1;
    letter-spacing: 1px;
    text-transform: uppercase;
    white-space: nowrap;
  }
</style>
</head>
<body>
  <div class="card">
    <svg class="card__shapes" width="1200" height="750" viewBox="0 0 1200 750">
      <defs>
        <linearGradient id="machineTone" x1="0" y1="0" x2="1" y2="1">
          <stop offset="0" stop-color="#7dbd52"/>
          <stop offset="1" stop-color="#9fd077"/>
        </linearGradient>
      </defs>
      <polygon class="panel" points="580,0 1200,0 1200,750 242,750 242,642 0,642 0,580" fill="var(--green)"/>
      <g role="img" aria-label="Illustration of an excavator arm and bucket in front of city buildings">
        <polygon points="560,150 820,150 1200,330 1200,750 640,750 660,420" fill="url(#machineTone)" opacity="0.75"/>
      </g>
    </svg>

    <div class="contact">
      <p class="contact__name">Tomas Verbelk</p>
      <p class="contact__title">Managing Director</p>
      <p class="contact__line">tomas@kravel.co.uk</p>
      <p class="contact__line">T: 020 5194 6381 &nbsp; M: 07845319027</p>
    </div>

    <div class="brand"><span class="brand__mark"></span>KRAVEL</div>

    <h1 class="heading">SERVICES</h1>
    <div class="website">www.kravel.co.uk</div>

    <ul class="services">
      <li class="services__item" style="left:866px;top:28px">Kitchen Renovations</li>
      <li class="services__item" style="left:824px;top:70px">Bathroom Renovations</li>
      <li class="services__item" style="left:782px;top:112px">House Renovations</li>
      <li class="services__item" style="left:740px;top:154px">Garage Conversions</li>
      <li class="services__item" style="left:698px;top:196px">Extensions</li>
      <li class="services__item" style="left:656px;top:238px">Loft Conversions</li>
      <li class="services__item" style="left:614px;top:280px">Conservatories</li>
      <li class="services__item" style="left:572px;top:322px">Carpentry</li>
      <li class="services__item" style="left:530px;top:364px">Tiling</li>
      <li class="services__item" style="left:488px;top:406px">Electrical</li>
      <li class="services__item" style="left:446px;top:448px">Plumbing &amp; Heating</li>
      <li class="services__item" style="left:404px;top:490px">Bricklaying</li>
      <li class="services__item" style="left:362px;top:532px">Landscaping</li>
      <li class="services__item" style="left:320px;top:574px">Decorating</li>
      <li class="services__item" style="left:278px;top:616px">Plastering</li>
    </ul>
  </div>
</body>
</html>
```